Dovenmarch Luxury Landscapes

A landscape business card.

Target Market(s)

Middle aged and up. Professionals.

Industry/Entity Type

Landscape

Contact Information for Business Card

Thornbeck

Colors
0054AA
0677BA
7BADD7
CADEEF
E8F1F8
0094D4
00A9DD
6FCCEA
C7EBF8
E9F6FB

Requirements
Must have
• The color blue and silver be very attractive
Nice to have
• An embossed logo. A watermark of a plant or something that indicates that we are a landscape company in the background of the backside where list of services are offered. . List of services on the back.
Should not have
• Red, yellow, orange.

```html
<!DOCTYPE html>
<html lang="en">
<head>
<meta charset="utf-8">
<title>Dovenmarch Luxury Landscapes – Business Card</title>
<link href="https://fonts.googleapis.com/css2?family=Open+Sans:wght@400;700&display=swap" rel="stylesheet">
<style>
  :root {
    --backdrop: #d6d6d6;
    --paper: #efefef;
    --royal: #1527a0;
    --silver: #d9deee;
    --ink: #1a1a1a;
  }
  * { margin: 0; padding: 0; box-sizing: border-box; }
  html, body {
    width: 1200px; height: 1051px; overflow: hidden;
    background: var(--backdrop);
    font-family: "Open Sans", Arial, sans-serif;
  }
  .card-set {
    position: absolute; left: 60px; top: 377px;
    display: flex; gap: 40px;
  }
  .card {
    width: 520px; height: 297px; position: relative;
  }
  .card-front {
    background: var(--paper);
    border-bottom: 3px solid var(--royal);
  }
  .holder-name {
    position: absolute; left: 40px; top: 128px;
    color: var(--royal); font-weight: 700; font-size: 25px;
  }
  .divider {
    position: absolute; left: 250px; top: 98px;
    width: 1.5px; height: 100px; background: var(--royal);
  }
  .contact {
    position: absolute; left: 270px; top: 98px;
    color: var(--ink); font-size: 16px; line-height: 22px;
    list-style: none;
  }
  .contact li { display: flex; align-items: center; gap: 6px; }
  .contact svg { width: 14px; height: 14px; fill: var(--royal); flex: none; }
  .address { margin-top: 4px; }
  .card-back {
    background: var(--royal);
    display: flex; align-items: center; justify-content: center;
  }
  .brand-name {
    color: var(--silver); font-weight: 700; font-size: 30px;
    text-transform: uppercase; text-align: center; line-height: 1.25;
    letter-spacing: 1px;
  }
</style>
</head>
<body>
  <div class="card-set">
    <section class="card card-front">
      <h1 class="holder-name">Marla Fenwick</h1>
      <div class="divider"></div>
      <ul class="contact">
        <li>
          <svg viewBox="0 0 24 24" aria-hidden="true"><path d="M6.6 10.8a15 15 0 0 0 6.6 6.6l2.2-2.2a1 1 0 0 1 1-.25 11.4 11.4 0 0 0 3.6.57 1 1 0 0 1 1 1V20a1 1 0 0 1-1 1A17 17 0 0 1 3 4a1 1 0 0 1 1-1h3.5a1 1 0 0 1 1 1c0 1.25.2 2.45.57 3.570a1 1 0 0 1-.25 1z"/></svg>
          902-555-LEAF
        </li>
        <li>
          <svg viewBox="0 0 24 24" aria-hidden="true"><circle cx="12" cy="12" r="10"/></svg>
          www.Dovenmarch.com
        </li>
        <li class="address">25A Hollin Road, Thornbeck,<br>Nova Scotia, B3K 2P4</li>
      </ul>
    </section>
    <section class="card card-back">
      <p class="brand-name">Dovenmarch<br>Luxury Landscapes</p>
    </section>
  </div>
</body>
</html>
```